International oil and gas consultancy needs a business card design

We need a business card design for a new oil and gas consultancy business based in Perth Australia. This is a professional services business and needs a moderately conservative type of business card. The business card also needs to be simple and uncluttered. The colour of the business logo is dark red (see attached file).
The front of the card should have a white background and mainly black lettering and perhaps some use of dark red and/or grey (your choice).
The back of the card should have a light grey background with dark red, black and or both dark red & black lettering (your choice).
Please find attached a clear brief of how I would like the business card designed.

Hello Everyone, I have slightly modified the brief. The main change is to incorporate some dark red and grey colours into the card, while still keeping the black lettering dominant. I have made the changes in the attached detailed brief document. Regards

Please note, the front of the card must say Pelwick Review Services (in addition to the logo).

Conservative

• brief has been updated. please refer to attachment for details.

Front of the card MUST say Pelwick Review Services (in addition to the logo)

```html
<!DOCTYPE html>
<html lang="en">
<head>
<meta charset="utf-8">
<title>Pelwick Review Services – Business Card</title>
<link rel="stylesheet" href="https://fonts.googleapis.com/css2?family=Arimo:wght@400;700&display=swap">
<style>
  :root {
    --brand-red: #9b1c20;
    --ink: #111111;
    --grey-text: #8a8a8a;
    --card-border: #5a5a5a;
    --front-bg: #ffffff;
    --back-bg: #f7f8fa;
    --row-line: #ececec;
    --arc-line: #e3e3e3;
    --divider: #e6e7ea;
  }
  * { box-sizing: border-box; margin: 0; padding: 0; }
  html, body {
    width: 1200px; height: 1000px; overflow: hidden;
    background: #ffffff;
    font-family: "Arimo", Arial, sans-serif;
    color: var(--ink);
  }
  .canvas { position: relative; width: 1200px; height: 1000px; }
  .card {
    position: absolute; left: 277px; width: 667px; height: 393px;
    border: 1px solid var(--card-border); overflow: hidden;
  }
  .card--front { top: 87px; background: var(--front-bg); }
  .card--back { top: 525px; background: var(--back-bg); }

  .front-arc { position: absolute; left: 0; top: 0; }

  .brand { position: absolute; display: flex; align-items: center; gap: 10px; }
  .brand__mark { width: 22px; height: 22px; background: var(--brand-red); }
  .brand__name { font-weight: 700; color: var(--brand-red); font-size: 64px; line-height: 1; letter-spacing: -1px; }
  .card--front .brand { left: 12px; top: 30px; }
  .card--back .brand { left: 52px; top: 134px; }

  .company-tag {
    position: absolute; left: 19px; top: 110px;
    color: var(--grey-text); font-size: 20px;
  }
  .abn { position: absolute; left: 14px; top: 371px; font-size: 10px; }

  .identity { position: absolute; left: 290px; width: 402px; text-align: center; }
  .identity__name { top: 44px; font-size: 26px; }
  .identity__title { top: 99px; font-size: 20px; }
  .identity__company { top: 150px; font-size: 20px; }

  .contact-row { position: absolute; left: 282px; height: 29px; display: flex; gap: 4px; }
  .contact-row__icon {
    width: 29px; height: 29px; border: 2px solid var(--row-line);
    display: flex; align-items: center; justify-content: center; background: #fff;
  }
  .contact-row__text {
    width: 360px; height: 29px; border: 2px solid var(--row-line); border-right: none;
    display: flex; align-items: center; justify-content: center;
    font-size: 17.5px; background: #fff;
  }
  .contact-row--region { top: 218px; }
  .contact-row--phone { top: 262px; }
  .contact-row--email { top: 308px; }
  .contact-row--web { top: 352px; }

  .tagline {
    position: absolute; left: 20px; width: 320px; top: 220px;
    text-align: center; font-size: 19px; line-height: 24px;
  }
  .back-divider {
    position: absolute; left: 357px; top: 58px; width: 1px; height: 258px;
    background: var(--divider);
  }
  .services { position: absolute; left: 411px; top: 105px; }
  .services__title { font-size: 23px; font-weight: 400; margin-bottom: 23px; }
  .services__list { list-style: none; }
  .services__item {
    position: relative; padding-left: 15px; font-size: 19px; height: 48px;
  }
  .services__item::before {
    content: ""; position: absolute; left: -6px; top: 7px;
    width: 8px; height: 8px; border-radius: 50%; background: var(--brand-red);
  }
</style>
</head>
<body>
<main class="canvas">

  <section class="card card--front" aria-label="Card front">
    <svg class="front-arc" width="667" height="393" aria-hidden="true">
      <circle cx="520" cy="108" r="236" fill="none" stroke="var(--arc-line)" stroke-width="2"/>
    </svg>

    <div class="brand">
      <span class="brand__mark"></span>
      <span class="brand__name">Pelwick</span>
    </div>
    <p class="company-tag">Pelwick Review Services</p>
    <p class="abn">ABN: 12 345 678 901</p>

    <p class="identity identity__name">Dana Merrow</p>
    <p class="identity identity__title">Director</p>
    <p class="identity identity__company">Pelwick Review Services</p>

    <div class="contact-row contact-row--region">
      <span class="contact-row__icon">
        <svg width="12" height="14" viewBox="0 0 12 14" aria-hidden="true"><path d="M6 1a4 4 0 0 0-4 4c0 3 4 8 4 8s4-5 4-8a4 4 0 0 0-4-4z" fill="none" stroke="var(--brand-red)" stroke-width="1.6"/><circle cx="6" cy="5" r="1.3" fill="var(--brand-red)"/></svg>
      </span>
      <span class="contact-row__text">Region: Australasia and South East Asia</span>
    </div>
    <div class="contact-row contact-row--phone">
      <span class="contact-row__icon">
        <svg width="15" height="15" viewBox="0 0 16 16" aria-hidden="true"><circle cx="8" cy="8" r="6.5" fill="none" stroke="var(--brand-red)" stroke-width="1.5"/><path d="M5.5 4.8l1.3 1.5-.7.9c.5 1 1.3 1.8 2.3 2.3l.9-.7 1.5 1.3-.8 1.1c-2.5-.4-4.6-2.5-5-5z" fill="var(--brand-red)"/></svg>
      </span>
      <span class="contact-row__text">Phone: +61&nbsp; (0)400 555 219</span>
    </div>
    <div class="contact-row contact-row--email">
      <span class="contact-row__icon">
        <svg width="15" height="11" viewBox="0 0 15 11" aria-hidden="true"><rect x="1" y="1" width="13" height="9" fill="none" stroke="var(--brand-red)" stroke-width="1.5"/><path d="M1 1l6.5 5L14 1" fill="none" stroke="var(--brand-red)" stroke-width="1.5"/></svg>
      </span>
      <span class="contact-row__text">Email: dana@pelwickreview.com</span>
    </div>
    <div class="contact-row contact-row--web">
      <span class="contact-row__icon">
        <svg width="15" height="15" viewBox="0 0 16 16" aria-hidden="true"><circle cx="8" cy="8" r="6.5" fill="none" stroke="var(--brand-red)" stroke-width="1.5"/><path d="M1.5 8h13M8 1.5c-2.5 3-2.5 10 0 13M8 1.5c2.5 3 2.5 10 0 13" fill="none" stroke="var(--brand-red)" stroke-width="1.2"/></svg>
      </span>
      <span class="contact-row__text">Website: www.pelwickreview.com</span>
    </div>
  </section>

  <section class="card card--back" aria-label="Card back">
    <div class="brand">
      <span class="brand__mark"></span>
      <span class="brand__name">Pelwick</span>
    </div>
    <p class="tagline">Special Finaanacial Consultants<br>to the Oil and Gas Industry</p>
    <div class="back-divider"></div>
    <div class="services">
      <h2 class="services__title">Services Provided:</h2>
      <ul class="services__list">
        <li class="services__item">Joint Venture Audits</li>
        <li class="services__item">Contract Audits</li>
        <li class="services__item">Operational Audits</li>
      </ul>
    </div>
  </section>

</main>
</body>
</html>
```